simple attractive bottled purified natural water label

Looking for a logo design, for a bottled water house brand.The Name of the water is "Toro-K" Natural Purified water I have attached 2 images, In the Mandel Image, I Like the top Left water design, the bold Red Name really stands out.I like the placement of the Font with the Natural Purified water,On the 2nd image Russian one, I again like the red bold, the bird flying out is interesting, not sure if a concept could rather use a seabird / gul or a albatros type, with the same effectThe blue colours in bother these designs are great.Many tahnks

Target Market(s)

Young crowd

Font styles to use
Sans Serif

Colors
0455a3
3276b5
ffffff
33a6d7
85cae6
85acd3
0692cd
ec1f27

Requirements
Must have
• some red in the label to make it pop.
• simple design
Nice to have
• the idea of a Gull ( Bird ) flying out to signify free pure natural.

```html
<!DOCTYPE html>
<html lang="en">
<head>
<meta charset="utf-8">
<title>Toro-K Natural Purified Water Label</title>
<link href="https://fonts.googleapis.com/css2?family=Oswald:wght@300;400;500&display=swap" rel="stylesheet">
<style>
  :root {
    --page: #f5f5f5;
    --label-blue: #1f4a9e;
    --label-blue-deep: #173c88;
    --ink-blue: #1c3f8c;
    --accent-red: #d8252c;
    --white: #ffffff;
    --clear: #eef2f8;
  }
  html, body {
    margin: 0;
    width: 900px;
    height: 1200px;
    overflow: hidden;
    background: var(--page);
  }
  .label {
    position: absolute;
    left: 175px;
    top: 55px;
    width: 550px;
    height: 1090px;
    background: var(--clear);
  }
  .label-band {
    position: absolute;
    left: 0;
    top: 0;
    width: 550px;
    height: 890px;
    background: linear-gradient(90deg, var(--label-blue-deep), var(--label-blue) 40%, var(--label-blue) 70%, var(--label-blue-deep));
  }
  .label-art {
    position: absolute;
    left: 0;
    top: 0;
  }
  .brand-name {
    font-family: "Oswald", sans-serif;
    font-weight: 400;
    font-size: 96px;
    fill: var(--white);
  }
  .descriptor {
    font-family: "Oswald", sans-serif;
    font-weight: 400;
    fill: var(--white);
    font-size: 46px;
  }
  .volume-main {
    font-family: "Oswald", sans-serif;
    font-weight: 500;
    font-size: 30px;
    fill: var(--accent-red);
  }
  .volume-sub {
    font-family: "Oswald", sans-serif;
    font-weight: 300;
    font-size: 14px;
    fill: var(--accent-red);
  }
  .claims {
    font-family: "Oswald", sans-serif;
    font-weight: 400;
    font-size: 30px;
    fill: var(--ink-blue);
  }
</style>
</head>
<body>
  <main class="label">
    <div class="label-band" role="img" aria-label="Blue label band with a repeating water drop pattern"></div>
    <svg class="label-art" width="550" height="1090" viewBox="0 0 550 1090">
      <path d="M0 846 C 110 818, 230 812, 330 838 S 480 880, 550 858 L550 1090 L0 1090 Z" fill="var(--accent-red)"/>
      <path d="M0 862 C 110 834, 230 828, 330 854 S 480 896, 550 874 L550 1090 L0 1090 Z" fill="var(--clear)"/>

      <text class="brand-name" x="275" y="430" text-anchor="middle">Toro-K</text>

      <rect class="rule-vertical" x="8" y="560" width="5" height="200" fill="var(--white)"/>
      <rect class="rule-horizontal" x="8" y="755" width="225" height="5" fill="var(--white)"/>
      <text class="descriptor" x="198" y="602" text-anchor="end">NATURAL</text>
      <text class="descriptor" x="198" y="668" text-anchor="end">PURIFIED</text>
      <text class="descriptor" x="198" y="733" text-anchor="end">WATER</text>

      <path d="M288 757 C 300 792, 356 830, 356 870 A68 68 0 1 1 220 870 C 220 830, 276 792, 288 757 Z" fill="var(--white)" stroke="var(--accent-red)" stroke-width="5"/>
      <text class="volume-main" x="288" y="880" text-anchor="middle">1 LITER</text>
      <text class="volume-sub" x="288" y="906" text-anchor="middle">33.8 FL OZ (2.11PT)</text>

      <text class="claims" x="288" y="990" text-anchor="middle">100% Purified water</text>
      <text class="claims" x="288" y="1030" text-anchor="middle">Natural pH</text>
      <text class="claims" x="288" y="1070" text-anchor="middle">Oxyzen Infused</text>
    </svg>
  </main>
</body>
</html>
```